High end business card design for custom homebuilding company

Looking for a high end business card design that is unique and elegant. Can use embossing, foil printing, laser die cutting, or any high end printing technique or high end paper. Will upload current design so you can see the logo and what we are using currently, but we want something more unique and elegant. I included our logo to help with design.

Target Market(s)

High end custom home buyers of $1.5 million plus homes. Also real estate developers of high end communities.

Industry/Entity Type

Business

Contact Information for Business Card

Double sided. We want something very elegant and expensive looking. We are looking to incorporate a combination of perhaps linen paper or a high end paper, with foil stamping or embossing/debossing to make the card look unique, but still elegant. We tend to use blacks and golds, but are open to any ideas. Looking for creative and unique design.

Colors

Designer to choose colors to be used in the design.

Requirements
Must have
• High end, elegant look. Can use foil, embossing, or high end papers like linen. We want to make the card unique and interesting, but elegant and expensive looking.
Nice to have
• I am including just some cards I saw that looked interesting for one reason or another. I like a clean elegant design and like both the clean white style, and the blacks. So not sure if we want a black design or white. Would like to see both.

```html
<!DOCTYPE html>
<html lang="en">
<head>
<meta charset="utf-8">
<title>Quillbrae Custom Homes – Business Card</title>
<link rel="stylesheet" href="https://fonts.googleapis.com/css2?family=Courgette&display=swap">
<style>
  :root {
    --backdrop: #6fbfb4;
    --paper: #fbfbf8;
    --ink: #2a2a28;
    --gold: #c9a43c;
    --gold-light: #ecd98a;
    --gold-deep: #9a7a22;
    --panel-light: #e6d48e;
    --panel-deep: #b99a3e;
  }
  * { box-sizing: border-box; margin: 0; padding: 0; }
  html, body {
    width: 1200px; height: 630px; overflow: hidden;
    background: var(--backdrop);
    font-family: "Courgette", cursive;
    color: var(--ink);
  }
  .canvas { position: relative; width: 1200px; height: 630px; }

  .card {
    position: absolute; top: 172px;
    width: 500px; height: 286px;
    background: var(--paper);
    box-shadow: 0 6px 18px rgba(0,0,0,.18);
    overflow: hidden;
  }
  .card--front { left: 70px; }
  .card--back { left: 630px; }
  .card svg.art { position: absolute; inset: 0; }

  .brand {
    position: absolute;
    display: flex; align-items: center; gap: 10px;
    color: var(--ink);
    white-space: nowrap;
  }
  .brand__dot {
    width: 16px; height: 16px; border-radius: 50%;
    background: var(--gold);
  }
  .brand__name { font-size: 22px; letter-spacing: .5px; }
  .card--front .brand { left: 22px; top: 26px; }
  .card--back .brand { left: 50%; top: 50%; transform: translate(-50%, -50%); }
  .card--back .brand__name { font-size: 28px; }

  .contact {
    position: absolute;
    display: flex; align-items: center; gap: 8px;
    font-size: 13px; white-space: nowrap;
  }
  .contact svg { width: 16px; height: 16px; flex: none; }
  .contact--mobile { left: 28px; top: 94px; }
  .contact--office { left: 28px; top: 124px; }
  .contact--web { left: 300px; top: 250px; }

  .holder { position: absolute; right: 44px; top: 26px; text-align: right; }
  .holder__name { font-size: 16px; }
  .holder__role { font-size: 11px; }

  .detail {
    position: absolute; right: 14px;
    display: flex; align-items: flex-start; gap: 10px;
    font-size: 11.5px; line-height: 1.2;
    text-align: left;
  }
  .detail svg { width: 16px; height: 16px; flex: none; }
  .detail--email { top: 90px; }
  .detail--address { top: 128px; }
  .detail__text { width: 110px; }
</style>
</head>
<body>
<main class="canvas">

  <section class="card card--front" aria-label="Card front">
    <svg class="art" viewBox="0 0 500 286" aria-hidden="true">
      <defs>
        <linearGradient id="panelFill" x1="0" y1="0" x2="1" y2="1">
          <stop offset="0" stop-color="var(--panel-light)"/>
          <stop offset="1" stop-color="var(--panel-deep)"/>
        </linearGradient>
      </defs>
      <path class="gold-panel"
            d="M0 176 L130 176 C150 176 150 204 176 204 L270 204 C292 204 296 214 296 232 L296 286 L0 286 Z"
            fill="url(#panelFill)" stroke="var(--gold-deep)" stroke-width="2"/>
    </svg>

    <div class="brand">
      <span class="brand__dot"></span>
      <span class="brand__name">Quillbrae Custom Homes</span>
    </div>

    <div class="contact contact--mobile">
      <svg viewBox="0 0 16 16"><rect x="4" y="1" width="8" height="14" rx="1.5" fill="none" stroke="var(--gold)" stroke-width="1.6"/><circle cx="8" cy="12.5" r=".9" fill="var(--gold)"/></svg>
      <span>+123-456-7890</span>
    </div>
    <div class="contact contact--office">
      <svg viewBox="0 0 16 16"><path d="M3 6 C3 3 13 3 13 6 L11 7 L10 5.5 L6 5.5 L5 7 Z" fill="var(--gold)"/><rect x="4" y="8" width="8" height="6" rx="1" fill="var(--gold)"/></svg>
      <span>1234567</span>
    </div>

    <div class="holder">
      <div class="holder__name">Holder Name</div>
      <div class="holder__role">Position</div>
    </div>

    <div class="detail detail--email">
      <span class="detail__text">name@email.com</span>
      <svg viewBox="0 0 16 16"><rect x="1.5" y="3.5" width="13" height="9" fill="none" stroke="var(--gold)" stroke-width="1.3"/><path d="M1.5 3.5 L8 9 L14.5 3.5" fill="none" stroke="var(--gold)" stroke-width="1.3"/></svg>
    </div>
    <div class="detail detail--address">
      <span class="detail__text">office address of holder</span>
      <svg viewBox="0 0 16 16"><path d="M8 15 C4 10 3 8 3 6 A5 5 0 0 1 13 6 C13 8 12 10 8 15 Z" fill="var(--gold)"/><circle cx="8" cy="6" r="1.8" fill="var(--paper)"/></svg>
    </div>

    <div class="contact contact--web">
      <svg viewBox="0 0 16 16"><g fill="none" stroke="var(--gold)" stroke-width="1.2"><circle cx="8" cy="8" r="6.5"/><ellipse cx="8" cy="8" rx="3" ry="6.5"/><path d="M1.5 8 H14.5 M2.5 4.8 H13.5 M2.5 11.2 H13.5"/></g></svg>
      <span>companywebsite.com</span>
    </div>
  </section>

  <section class="card card--back" aria-label="Card back">
    <svg class="art" viewBox="0 0 500 286" aria-hidden="true">
      <defs>
        <linearGradient id="foil" x1="0" y1="0" x2="1" y2="0">
          <stop offset="0" stop-color="var(--gold-deep)"/>
          <stop offset=".35" stop-color="var(--gold-light)"/>
          <stop offset=".65" stop-color="var(--gold)"/>
          <stop offset="1" stop-color="var(--gold-deep)"/>
        </linearGradient>
      </defs>
      <path class="foil-line" d="M0 96 L150 96 C210 96 220 42 290 42 L500 42"
            fill="none" stroke="url(#foil)" stroke-width="6"/>
      <path class="foil-line" d="M0 254 L200 254 C270 254 280 192 350 192 L500 192"
            fill="none" stroke="url(#foil)" stroke-width="6"/>
    </svg>

    <div class="brand">
      <span class="brand__dot"></span>
      <span class="brand__name">Quillbrae Custom Homes</span>
    </div>
  </section>

</main>
</body>
</html>
```